The Velvet Magpie business card

I need a business card for my makeup artist business. I specialise in bridal, glamour, formal and special occasion makeup.
I am a mobile makeup artist who caters for every from nowra to sydney.
I do the following services:
Bridal makeup
airbrush makeup
special occasion
formals
hens nights/ girls night
makeup lesson
makeup for all ages from flower girl to Nanna of the bride!
photoshoot makeup
SPFX

I would like the card to portray a very professional sleek makeup business. I would also like another version of the card directed especially towards brides.

Please see my website to understand colours etc www.thevelvetmagpie.com

Industry/Entity Type

Business

Contact Information for Business Card

The Velvet Magpie
Professional Makeup Artist
Marguerite Olvey
0412083946
info@thevelvetmagpie.com
www.thevelvetmagpie.com
www.facebook.com/thevelvetmagpie

```html
<!DOCTYPE html>
<html lang="en">
<head>
<meta charset="utf-8">
<title>The Velvet Magpie – Business Card</title>
<link href="https://fonts.googleapis.com/css2?family=Amatic+SC:wght@700&family=Roboto:wght@400;500;700&display=swap" rel="stylesheet">
<style>
  :root {
    --magenta: #e0197d;
    --magenta-soft: #f27ab4;
    --ink: #2b2b2b;
    --paper: #ffffff;
    --backdrop: #ecebea;
  }
  * { box-sizing: border-box; margin: 0; padding: 0; }
  html, body { width: 1200px; height: 871px; overflow: hidden; }
  body {
    background: var(--backdrop);
    font-family: "Roboto", Arial, sans-serif;
    position: relative;
  }
  .card {
    position: absolute;
    top: 106px;
    width: 380px;
    height: 660px;
    border-radius: 26px;
    overflow: hidden;
    box-shadow: 0 10px 28px rgba(0,0,0,.18);
  }
  /* Front */
  .card-front { left: 190px; background: var(--paper); }
  .top-rule {
    position: absolute; left: 0; right: 0; top: 22px;
    height: 6px; background: var(--magenta);
  }
  .brand {
    position: absolute; left: 34px; top: 58px;
    font-family: "Amatic SC", cursive;
    font-weight: 700;
    font-size: 52px;
    letter-spacing: 2px;
    color: var(--magenta);
    line-height: 1;
  }
  .person { position: absolute; left: 34px; top: 178px; }
  .person-name { font-size: 25px; font-weight: 400; color: var(--ink); }
  .person-role { font-size: 15px; font-weight: 500; color: var(--magenta); margin-top: 4px; }
  .contacts { position: absolute; left: 34px; top: 276px; list-style: none; }
  .contacts li {
    display: flex; align-items: center; gap: 10px;
    font-size: 18px; color: var(--ink); height: 32px;
  }
  .contact-icon {
    width: 20px; height: 20px; border-radius: 50%;
    background: var(--magenta);
    display: flex; align-items: center; justify-content: center;
    flex: none;
  }
  .floral-band {
    position: absolute; left: 0; right: 0; bottom: 0; height: 190px;
    background: radial-gradient(ellipse at 70% 100%, var(--magenta) 0%, var(--magenta-soft) 38%, rgba(255,255,255,0) 72%);
  }
  /* Back */
  .card-back {
    left: 630px;
    background: var(--magenta);
    padding: 10px;
    display: grid;
    grid-template-columns: 1fr 1fr;
    grid-template-rows: 240px 1fr 1fr;
    gap: 8px;
  }
  .photo { border-radius: 4px; }
  .photo-party {
    grid-column: 1 / 3; border-radius: 18px 18px 4px 4px;
    background: linear-gradient(180deg, #5b4a3c 0%, #3a4aa0 55%, #2f3f9a 100%);
  }
  .photo-application { background: linear-gradient(135deg, #d8b9a0 0%, #8a6a55 100%); }
  .photo-portrait { background: linear-gradient(135deg, #c9a27e 0%, #e3c7ae 100%); }
  .photo-detail { background: linear-gradient(135deg, #bfa08a 0%, #7d6656 100%); border-radius: 4px 4px 4px 18px; }
  .photo-glamour { background: linear-gradient(135deg, #c89a6c 0%, #e6c8b2 100%); border-radius: 4px 4px 18px 4px; }
</style>
</head>
<body>

<section class="card card-front">
  <div class="top-rule"></div>
  <div class="brand">The Velvet Magpie</div>
  <div class="person">
    <div class="person-name">Marguerite Olvey</div>
    <div class="person-role">Professional Makeup Artist</div>
  </div>
  <ul class="contacts">
    <li>
      <span class="contact-icon">
        <svg width="12" height="12" viewBox="0 0 24 24"><path fill="#fff" d="M6.6 10.8a15 15 0 006.6 6.6l2.2-2.2c.3-.3.7-.4 1-.2 1.1.4 2.3.6 3.6.6.6 0 1 .4 1 1V20c0 .6-.4 1-1 1A17 17 0 013 4c0-.6.4-1 1-1h3.5c.6 0 1 .4 1 1 0 1.3.2 2.5.6 3.6.1.3 0 .7-.2 1z"/></svg>
      </span>
      0412083946
    </li>
    <li>
      <span class="contact-icon">
        <svg width="12" height="12" viewBox="0 0 24 24"><rect x="3" y="6" width="18" height="12" rx="1" fill="none" stroke="#fff" stroke-width="2"/><path d="M3 7l9 6 9-6" fill="none" stroke="#fff" stroke-width="2"/></svg>
      </span>
      info@thevelvetmagpie.com
    </li>
    <li>
      <span class="contact-icon">
        <svg width="12" height="12" viewBox="0 0 24 24"><circle cx="12" cy="12" r="9" fill="none" stroke="#fff" stroke-width="2"/><path d="M3 12h18M12 3c3 3 3 15 0 18M12 3c-3 3-3 15 0 18" fill="none" stroke="#fff" stroke-width="1.6"/></svg>
      </span>
      www.thevelvetmagpie.com
    </li>
    <li>
      <span class="contact-icon"></span>
      / thevelvetmagpie
    </li>
  </ul>
  <div class="floral-band" role="img" aria-label="Pink floral swirl ornament"></div>
</section>

<section class="card card-back">
  <div class="photo photo-party" role="img" aria-label="Photo of a bridal party in blue dresses holding bouquets"></div>
  <div class="photo photo-application" role="img" aria-label="Photo of makeup being applied"></div>
  <div class="photo photo-portrait" role="img" aria-label="Portrait photo showing finished makeup"></div>
  <div class="photo photo-detail" role="img" aria-label="Photo of a hairstyle detail"></div>
  <div class="photo photo-glamour" role="img" aria-label="Photo of glamour makeup with red lips"></div>
</section>

</body>
</html>
```